Holvik Cabinets Quality Custom Built Kitchens, Vanity Units, Robes ect

Hi,
Was after a new design for our business cards,
we are a cabinet making business and pride ourselves in quality custom built Kitchens, Vanity units, robes ect.
we have been around for over 20 years and we are trying to modernize our card logo.
Looking for something eye catching, bold and exciting
family ran and operated business, we work with builders and also have a large private clientel.

Thanks

Industry/Entity Type

Business

Contact Information for Business Card

Holvik Cabinets

Font styles to use
Serif
Script

Requirements
Must have
• Corinne 0461735928 hvcabinets@mailvane.com
• Po Box 2786
• 5B Wattlebark Court Glenmorrow Vic 3871
• Phone (03)59286417 Fax (03) 59286942
Nice to have
• Quality Custom Built Kitchens & Vanity Units

```html
<!DOCTYPE html>
<html lang="en">
<head>
<meta charset="utf-8">
<title>Holvik Cabinets – Business Cards</title>
<link href="https://fonts.googleapis.com/css2?family=Marcellus&family=Great+Vibes&family=Open+Sans:wght@400&display=swap" rel="stylesheet">
<style>
  :root {
    --backdrop: #ece7df;
    --maroon: #3b1113;
    --sand: #c8bca6;
    --cream: #dccfb6;
    --ink: #4a2a22;
    --flourish: #6a4340;
  }
  html, body {
    margin: 0;
    width: 1200px;
    height: 800px;
    overflow: hidden;
    background: var(--backdrop);
  }
  .sheet {
    position: relative;
    width: 1200px;
    height: 800px;
  }
  .card {
    position: absolute;
    top: 250px;
    width: 520px;
    height: 300px;
    background: var(--sand);
    overflow: hidden;
    box-shadow: 0 6px 18px rgba(60, 30, 20, 0.18);
  }
  .card--front { left: 50px; }
  .card--back  { left: 630px; }

  .card__band {
    position: absolute;
    left: 0; top: 0;
    width: 100%;
    height: 185px;
    background: var(--maroon);
  }
  .card__rule {
    position: absolute;
    left: 0; top: 176px;
    width: 100%;
    height: 1px;
    background: var(--cream);
    opacity: 0.7;
  }

  /* Front */
  .front__title {
    position: absolute;
    top: 42px; left: 0; width: 100%;
    text-align: center;
    font: 40px "Marcellus", serif;
    color: var(--cream);
    margin: 0;
    letter-spacing: 0.5px;
  }
  .front__ornament {
    position: absolute;
    top: 52px;
    width: 30px; height: 24px;
    background: var(--flourish);
    border-radius: 4px;
  }
  .front__ornament--left  { left: 72px; }
  .front__ornament--right { right: 72px; }
  .front__tagline {
    position: absolute;
    top: 112px; left: 0; width: 100%;
    text-align: center;
    font: 20px "Marcellus", serif;
    color: var(--cream);
    margin: 0;
  }
  .front__address {
    position: absolute;
    top: 196px; left: 22px;
    margin: 0;
    font: 13px/1.45 "Open Sans", sans-serif;
    color: var(--ink);
    font-style: normal;
  }
  .front__numbers {
    position: absolute;
    bottom: 18px; right: 22px;
    margin: 0;
    text-align: right;
    font: 14px/1.5 "Open Sans", sans-serif;
    color: var(--ink);
  }

  /* Back */
  .back__flourish {
    position: absolute;
    top: 0; left: 40px;
    width: 170px; height: 150px;
    background: radial-gradient(ellipse at center, rgba(120, 85, 80, 0.45), rgba(59, 17, 19, 0) 70%);
  }
  .back__brand {
    position: absolute;
    top: 22px; right: 22px;
    text-align: right;
    color: var(--cream);
  }
  .back__name-of-business {
    margin: 0;
    font: 20px "Marcellus", serif;
  }
  .back__tagline {
    margin: 2px 0 0;
    font: 12px "Marcellus", serif;
  }
  .back__person {
    position: absolute;
    top: 112px; right: 28px;
    margin: 0;
    font: 52px "Great Vibes", cursive;
    color: var(--cream);
  }
  .back__contact {
    position: absolute;
    top: 196px; right: 22px;
    margin: 0;
    text-align: right;
    font: 20px/1.45 "Open Sans", sans-serif;
    color: var(--maroon);
  }
</style>
</head>
<body>
<main class="sheet">

  <section class="card card--front" aria-label="Business card front">
    <div class="card__band"></div>
    <div class="card__rule"></div>
    <div class="front__ornament front__ornament--left" role="img" aria-label="Small decorative flourish"></div>
    <h1 class="front__title">Holvik Cabinets</h1>
    <div class="front__ornament front__ornament--right" role="img" aria-label="Small decorative flourish"></div>
    <p class="front__tagline">Quality Custom Built Kitchens &amp; Vanity Units</p>
    <address class="front__address">
      Po Box 2786<br>
      5B Wattlebark Court<br>
      Glenmorrow Vic 3871
    </address>
    <p class="front__numbers">
      Phone (03) 59286417<br>
      Fax (03) 59286942
    </p>
  </section>

  <section class="card card--back" aria-label="Business card back">
    <div class="card__band"></div>
    <div class="card__rule"></div>
    <div class="back__flourish" role="img" aria-label="Large faint swirl decoration"></div>
    <div class="back__brand">
      <p class="back__name-of-business">Holvik Cabinets</p>
      <p class="back__tagline">Quality Custom Built Kitchens &amp; Vanity Units</p>
    </div>
    <p class="back__person">Corinne</p>
    <p class="back__contact">
      0461735928<br>
      hvcabinets@mailvane.com
    </p>
  </section>

</main>
</body>
</html>
```